Power point Presentation Template 2

I am looking a professionally designed Powerpoint Presentation template for my company. We are Information Technology Company. I have attached the Logo. The Logo will also give an indication of which colours to be used in the design.

Target Market(s)

Information and Communication Technology

Requirements
Must have
• All ideas welcomed
Nice to have
• Professional Look and Feel

```html
<!DOCTYPE html>
<html lang="en">
<head>
<meta charset="utf-8">
<title>Novara Technologies – Presentation Template</title>
<link href="https://fonts.googleapis.com/css2?family=Titillium+Web:ital,wght@0,300;0,400;0,600;0,700;1,400&display=swap" rel="stylesheet">
<style>
:root{
  --orange:#ff8200;
  --orange-soft:#ffb266;
  --dark:#3c3c3e;
  --ink:#231f20;
  --grey:#808285;
  --grey-mid:#a7a9ac;
  --grey-light:#d1d2d4;
  --paper:#ffffff;
  --canvas:#f1f1f1;
}
*{box-sizing:border-box;margin:0;padding:0}
html,body{width:890px;height:1200px;overflow:hidden}
body{background:var(--canvas);font-family:"Titillium Web",Arial,sans-serif;color:var(--dark);position:relative}
.slide{position:absolute;width:285px;height:161px;background:var(--paper);overflow:hidden;box-shadow:0 1px 3px rgba(0,0,0,.12)}
.abs{position:absolute}
.title{position:absolute;font-weight:700;font-size:17px;line-height:1;color:var(--ink);letter-spacing:.01em}
.title .hl{color:var(--orange)}
.body{position:absolute;font-size:4.6px;line-height:1.38;color:var(--grey);text-align:justify}
.body p+p{margin-top:3px}
.sub{position:absolute;font-size:7px;color:var(--ink)}
.photo{position:absolute}
svg{position:absolute;overflow:visible}

/* wordmark */
.logo{position:absolute;display:flex;align-items:center;gap:.22em;color:var(--orange);font-weight:700;line-height:.9}
.logo .dot{width:.7em;height:.7em;border-radius:50%;background:var(--orange);flex:none}
.logo .name{display:block;font-size:1em;letter-spacing:.03em}
.logo .tag{display:block;font-size:.3em;letter-spacing:.42em;margin-top:.15em}

/* slide: cover photo */
.cover .photo{inset:0;background:linear-gradient(100deg,#f4f4f4 0%,#e4e4e4 45%,#b9b9b9 100%)}
.cover .accent{left:0;top:105px;width:9px;height:56px;background:var(--orange)}
.cover .deck{left:19px;top:111px;font-size:11px;color:var(--ink)}
.cover .deck-sub{left:19px;top:126px;font-size:6.5px;color:var(--orange)}

/* slide: orange title */
.titlecard .band{left:0;top:0;width:285px;height:128px;background:var(--orange)}
.titlecard .rule{left:0;top:128px;width:285px;height:2px;background:var(--dark)}
.titlecard h1{position:absolute;left:17px;top:22px;font-size:17px;font-weight:700;color:#fff;line-height:1}
.titlecard .s1{left:19px;top:44px;font-size:9px;color:#fff}
.titlecard .s2{left:19px;top:57px;font-size:7.5px;color:#fff}
.titlecard .dash{left:20px;top:74px;width:19px;height:2px;background:#fff}
.titlecard .skyline{right:4px;bottom:33px;width:120px;height:40px;background:linear-gradient(180deg,rgba(255,210,150,.35),rgba(255,210,150,.75))}
.titlecard .web{left:8px;top:138px;font-size:6.5px;color:var(--dark);line-height:1.3}

/* slide: section */
.section .pattern{inset:0;background:radial-gradient(circle at 50% 50%,#fff 0 28%,var(--orange) 29% 60%,#fff 61%)}
.section .plate{left:98px;top:37px;width:92px;height:90px;background:#fff;border-radius:22px}
.section .num{left:109px;top:84px;font-size:27px;font-weight:700;color:var(--dark);line-height:1}
.section .bar{left:139px;top:86px;width:1px;height:24px;background:var(--dark)}
.section .lbl{left:145px;top:86px;font-size:8px;font-weight:700;color:var(--grey);line-height:1.3}

/* slide: about */
.about .panel{left:0;top:0;width:141px;height:161px;background:var(--grey)}
.about .globe{left:25px;top:34px;width:92px;height:92px;border-radius:50%;background:radial-gradient(circle,#9a9b9e,#8a8b8e)}

/* agenda */
.agenda{width:586px;height:332px}
.agenda .side{left:501px;top:0;width:85px;height:332px;background:var(--orange)}
.agenda h2{position:absolute;left:26px;top:26px;font-size:37px;font-weight:700;color:var(--ink);line-height:1}
.agenda .item{position:absolute;left:37px;width:210px}
.agenda .item h3{font-size:14px;font-weight:400;color:var(--ink);line-height:1}
.agenda .item p{margin:8px 0 0 11px;font-size:10px;line-height:1.32;color:var(--grey);text-align:justify}

/* dark title */
.darkphoto .photo{inset:0;background:linear-gradient(120deg,#1c1c1e 0%,#3a3a3d 55%,#252527 100%)}
.darkphoto .quote{left:148px;top:61px;width:137px;height:71px;background:rgba(40,40,42,.88)}
.darkphoto .qtext{left:189px;top:83px;width:90px;font-size:6.5px;font-style:italic;color:#fff;line-height:1.3;text-align:justify}
.darkphoto .qmark{font-size:22px;font-weight:700;font-style:italic;color:#fff;line-height:1}

/* comparison */
.compare .box{position:absolute;top:33px;width:124px;height:114px;padding:7px 10px}
.compare .box h4{font-size:6.5px;font-weight:700;text-align:center;color:var(--ink)}
.compare .box p{font-size:4.4px;line-height:1.35;margin-top:5px;text-align:justify}
.compare .prob{left:12px;background:var(--grey-light)}
.compare .prob p{color:var(--grey)}
.compare .sol{left:147px;background:var(--orange)}
.compare .sol h4,.compare .sol p{color:#fff}

/* team */
.team .pic{position:absolute;top:43px;width:57px;height:83px;background:linear-gradient(160deg,#e7e9ec,#9aa3ad)}
.team .who{position:absolute;top:128px;width:57px;font-size:4.8px;line-height:1.25;color:var(--dark);padding:1px 4px}
.team .who.on{background:var(--orange);color:#fff}

/* pie legend */
.legend{position:absolute;left:136px;width:146px;height:31px;border-radius:4px;display:flex;align-items:center;gap:8px;padding:0 10px;color:#fff;font-size:4.8px;line-height:1.3}
</style>
</head>
<body>

<!-- Row 1 -->
<section class="slide cover" style="left:7px;top:17px">
  <div class="photo" role="img" aria-label="Black and white photo of hands folded beside a laptop on a desk with a small plant"></div>
  <div class="logo" style="left:14px;top:52px;font-size:28px"><span class="dot"></span><span><span class="name">NOVARA</span><span class="tag">TECHNOLOGIES</span></span></div>
  <div class="abs accent"></div>
  <div class="abs deck">Your Slides Deck Name</div>
  <div class="abs deck-sub">Your Slides Deck Name</div>
</section>

<section class="slide titlecard" style="left:302px;top:17px">
  <div class="abs band"></div>
  <div class="abs rule"></div>
  <h1>YOUR SLIDES DECK NAME</h1>
  <div class="abs s1">Your Slides Sub Deck Name</div>
  <div class="abs s2">2019</div>
  <div class="abs dash"></div>
  <div class="abs skyline" role="img" aria-label="Light orange city skyline illustration"></div>
  <div class="abs web">www.yourwebsite.com<br>@yourfbname</div>
  <div class="logo" style="right:12px;top:136px;font-size:14px"><span class="dot"></span><span><span class="name">NOVARA</span><span class="tag">TECHNOLOGIES</span></span></div>
</section>

<section class="slide section" style="left:597px;top:17px">
  <div class="abs pattern" role="img" aria-label="Orange diagonal rounded strokes and dots pattern"></div>
  <div class="abs plate"></div>
  <div class="logo" style="left:106px;top:54px;font-size:14px"><span class="dot"></span><span><span class="name">NOVARA</span><span class="tag">TECHNOLOGIES</span></span></div>
  <div class="abs num">01</div>
  <div class="abs bar"></div>
  <div class="abs lbl">THE<br>COMPANY</div>
</section>

<!-- Row 2 -->
<section class="slide timeline" style="left:7px;top:185px">
  <div class="title" style="left:12px;top:12px">TIME<span class="hl">LINE</span></div>
  <div class="logo" style="right:14px;top:16px;font-size:10px"><span class="dot"></span><span><span class="name">NOVARA</span><span class="tag">TECHNOLOGIES</span></span></div>
  <svg width="285" height="161" viewBox="0 0 285 161" style="left:0;top:0">
    <polygon points="110,39 154,64 154,114 110,139 66,114 66,64" fill="#6b6e73" role="img" aria-label="Photo of an analytics dashboard on a screen"/>
    <g font-family="Titillium Web, sans-serif" text-anchor="middle">
      <g>
        <polygon points="44,55 73,72 73,106 44,123 15,106 15,72" fill="#fff" stroke="#ff8200" stroke-width="4"/>
        <polygon points="76,86 80,89 76,92" fill="#ff8200"/>
        <text x="44" x2="" y="82" font-size="7" font-weight="700" fill="#231f20">2016</text>
        <text x="44" y="91" font-size="4.6" fill="#808285">Lorem ipsum</text>
        <text x="44" y="97" font-size="4.6" fill="#808285">dolor sit amet,</text>
        <text x="44" y="103" font-size="4.6" fill="#808285">consectetuer</text>
      </g>
      <g>
        <polygon points="110,55 139,72 139,106 110,123 81,106 81,72" fill="#ff8200" stroke="#ffb266" stroke-width="4"/>
        <polygon points="142,86 146,89 142,92" fill="#ff8200"/>
        <text x="110" y="82" font-size="7" font-weight="700" fill="#fff">2017</text>
        <text x="110" y="91" font-size="4.6" fill="#fff">Lorem ipsum</text>
        <text x="110" y="97" font-size="4.6" fill="#fff">dolor sit amet,</text>
        <text x="110" y="103" font-size="4.6" fill="#fff">consectetuer</text>
      </g>
      <g>
        <polygon points="176,55 205,72 205,106 176,123 147,106 147,72" fill="#fff" stroke="#ff8200" stroke-width="4"/>
        <polygon points="208,86 212,89 208,92" fill="#ff8200"/>
        <text x="176" y="82" font-size="7" font-weight="700" fill="#231f20">2018</text>
        <text x="176" y="91" font-size="4.6" fill="#808285">Lorem ipsum</text>
        <text x="176" y="97" font-size="4.6" fill="#808285">dolor sit amet,</text>
        <text x="176" y="103" font-size="4.6" fill="#808285">consectetuer</text>
      </g>
      <g>
        <polygon points="242,55 271,72 271,106 242,123 213,106 213,72" fill="#fff" stroke="#ff8200" stroke-width="4"/>
        <polygon points="274,86 278,89 274,92" fill="#ff8200"/>
        <text x="242" y="82" font-size="7" font-weight="700" fill="#231f20">2019</text>
        <text x="242" y="91" font-size="4.6" fill="#808285">Lorem ipsum</text>
        <text x="242" y="97" font-size="4.6" fill="#808285">dolor sit amet,</text>
        <text x="242" y="103" font-size="4.6" fill="#808285">consectetuer</text>
      </g>
    </g>
  </svg>
</section>

<section class="slide about" style="left:7px;top:354px">
  <div class="abs panel"></div>
  <div class="abs globe" role="img" aria-label="White network sphere with an orange letter M inside"></div>
  <div class="title" style="left:185px;top:14px">ABOUT <span class="hl">US</span></div>
  <div class="body" style="left:150px;top:42px;width:124px">
    <p>Lorem ipsum dolor sit amet, consectetuer adipiscing elit, sed diam nonummy nibh euismod tincidunt ut laoreet dolore magna aliquam erat volutpat.</p>
    <p>Ut wisi enim ad minim veniam, quis nostrud exerci tation ullamcorper suscipit lobortis nisl ut aliquip ex ea commodo consequat. Duis autem vel eum iriure dolor in hendrerit in vulputate velit esse molestie consequat, vel illum dolore eu feugiat nulla facilisis at vero eros et</p>
    <p>Lorem ipsum dolor sit amet, consectetuer adipiscing elit, sed diam nonummy.</p>
  </div>
  <div class="logo" style="right:10px;top:138px;font-size:12px"><span class="dot"></span><span><span class="name">NOVARA</span><span class="tag">TECHNOLOGIES</span></span></div>
</section>

<section class="slide agenda" style="left:302px;top:185px">
  <div class="abs side"></div>
  <h2>AGENDA</h2>
  <div class="item" style="top:88px"><h3>01. Overview</h3><p>Lorem ipsum dolor sit amet, consectetuer adipiscing elit, sed diam nonummy nibh euismod tincidunt ut</p></div>
  <div class="item" style="top:163px"><h3>02. About us</h3><p>Lorem ipsum dolor sit amet, consectetuer adipiscing elit, sed diam nonummy nibh euismod tincidunt ut</p></div>
  <div class="item" style="top:238px"><h3>03. Meet our team</h3><p>Lorem ipsum dolor sit amet, consectetuer adipiscing elit, sed diam nonummy nibh euismod tincidunt ut</p></div>
  <svg width="586" height="332" viewBox="0 0 586 332" style="left:0;top:0">
    <g fill="none" stroke="#c4c5c7" stroke-width="1.6">
      <path d="M339 36 C420 30 405 130 437 135"/>
      <path d="M391 81 C420 85 415 140 437 142"/>
      <path d="M315 98 C400 110 410 148 437 150"/>
      <path d="M350 158 C400 158 410 158 437 158"/>
      <path d="M393 140 C415 150 420 164 437 166"/>
      <path d="M390 205 C420 200 420 176 437 174"/>
      <path d="M306 218 C400 240 420 190 437 182"/>
      <path d="M346 278 C410 280 415 200 437 190"/>
      <path d="M393 272 C425 260 425 205 437 198"/>
    </g>
    <g fill="#ff8200" stroke="#d1d2d4">
      <circle cx="320" cy="36" r="19" stroke-width="3"/>
      <circle cx="361" cy="81" r="30" stroke-width="4"/>
      <circle cx="296" cy="98" r="19" stroke-width="3"/>
      <circle cx="317" cy="158" r="33" stroke-width="4"/>
      <circle cx="375" cy="140" r="18" stroke-width="3"/>
      <circle cx="366" cy="205" r="24" stroke-width="4"/>
      <circle cx="284" cy="218" r="22" stroke-width="3"/>
      <circle cx="314" cy="278" r="32" stroke-width="4"/>
      <circle cx="380" cy="272" r="13" stroke-width="3"/>
    </g>
    <g fill="#fff" stroke="none">
      <rect x="312" y="33" width="4" height="11"/><rect x="318" y="29" width="4" height="15"/><rect x="324" y="36" width="4" height="8"/>
      <circle cx="361" cy="92" r="3"/>
      <rect x="301" y="143" width="32" height="21" rx="2" fill="none" stroke="#fff" stroke-width="2"/>
      <rect x="296" y="166" width="42" height="3" rx="1"/>
      <path d="M375 130 a6 6 0 0 1 6 6 c0 5 -6 12 -6 12 c0 0 -6 -7 -6 -12 a6 6 0 0 1 6 -6z"/>
      <path d="M354 212 h24 a7 7 0 0 0 -2 -13 a9 9 0 0 0 -17 -2 a7 7 0 0 0 -5 15z"/>
      <path d="M274 212 h7 l2 3 h11 v12 h-20z"/>
      <rect x="304" y="262" width="20" height="32" rx="3" fill="none" stroke="#fff" stroke-width="2.5"/>
      <circle cx="380" cy="272" r="5.5" fill="none" stroke="#fff" stroke-width="2"/>
    </g>
    <g fill="none" stroke="#fff" stroke-width="2.5" stroke-linecap="round">
      <path d="M347 79 a20 20 0 0 1 28 0"/><path d="M352 85 a12 12 0 0 1 18 0"/>
      <circle cx="296" cy="98" r="8" stroke-width="1.5"/><path d="M288 98 h16 M296 90 v16" stroke-width="1.2"/>
      <path d="M366 201 v9 m-4 -4 l4 4 l4 -4" stroke="#ff8200" stroke-width="2"/>
    </g>
    <rect x="437" y="118" width="131" height="90" rx="4" fill="#c8c9cb"/>
    <rect x="443" y="124" width="119" height="74" fill="#ececec"/>
    <circle cx="502" cy="203" r="3" fill="#3c3c3e"/>
    <path d="M494 208 h16 l3 14 h-22z" fill="#b5b6b8"/>
    <rect x="482" y="221" width="40" height="4" rx="1" fill="#a7a9ac"/>
  </svg>
  <div class="logo" style="left:448px;top:148px;font-size:20px"><span class="dot"></span><span><span class="name">NOVARA</span><span class="tag">TECHNOLOGIES</span></span></div>
</section>

<!-- Row 3 -->
<section class="slide darkphoto" style="left:7px;top:525px">
  <div class="photo" role="img" aria-label="Dark photo of a hand holding a smartphone showing a video app"></div>
  <div class="logo" style="right:9px;top:12px;font-size:15px"><span class="dot"></span><span><span class="name">NOVARA</span><span class="tag">TECHNOLOGIES</span></span></div>
  <svg width="26" height="18" viewBox="0 0 26 18" style="left:7px;top:30px"><path d="M4 17 h18 a5 5 0 0 0 -1 -10 a8 8 0 0 0 -15 -1 a5 5 0 0 0 -2 11z" fill="#fff"/><path d="M13 6 v8 m-4 -4 l4 4 l4 -4" stroke="#2a2a2a" stroke-width="2.2" fill="none"/></svg>
  <div class="title" style="left:8px;top:58px;color:#fff">YOUR TITLE</div>
  <div class="sub" style="left:8px;top:79px;color:#fff">Subtitle</div>
  <div class="body" style="left:8px;top:98px;width:110px;color:#fff;font-size:5px">Lorem ipsum dolor sit amet, consectetuer adipiscing elit, sed diam nonummy nibh euismod tincidunt ut laoreet dolore magna aliquam erat volutpat. Ut wisi enim ad minim veniam, quis nostrud exerci tation ullamcorper suscipit lobortis</div>
  <div class="abs quote"></div>
  <div class="abs qmark" style="left:174px;top:66px">//</div>
  <div class="abs qtext">Lorem ipsum dolor sit amet, consectetuer adipiscing elit, sed diam nonummy nibh euismod</div>
  <div class="abs qmark" style="left:206px;top:110px">//</div>
</section>

<section class="slide" style="left:302px;top:525px">
  <div class="title" style="left:13px;top:12px">YOUR <span class="hl">TITLE</span></div>
  <div class="logo" style="right:10px;top:14px;font-size:15px"><span class="dot"></span><span><span class="name">NOVARA</span><span class="tag">TECHNOLOGIES</span></span></div>
  <div class="sub" style="left:19px;top:37px">Subtitle</div>
  <div class="abs" style="left:2px;top:52px;width:22px;height:94px;background:var(--orange)"></div>
  <div class="body" style="left:36px;top:52px;width:238px">
    <p>Lorem ipsum dolor sit amet, consectetuer adipiscing elit, sed diam nonummy nibh euismod tincidunt ut laoreet dolore magna aliquam erat volutpat. Ut wisi enim ad minim veniam, quis nostrud exerci tation ullamcorper suscipit lobortis nisl ut aliquip ex ea commodo consequat.</p>
    <p>Duis autem vel eum iriure dolor in hendrerit in vulputate velit esse molestie consequat, vel illum dolore eu feugiat nulla facilisis at vero eros et accumsan et iusto odio dignissim qui blandit praesent luptatum zzril delenit augue duis dolore te feugait nulla facilisi.</p>
    <p>Lorem ipsum dolor sit amet, cons ectetuer adipiscing elit, sed diam nonummy nibh euismod tincidunt ut laoreet dolore magna aliquam erat volutpat. Ut wisi enim ad minim veniam, quis nostrud exerci tation ullamcorper suscipit lobortis nisl ut aliquip ex ea commodo consequat.</p>
    <p>drerit in vulputate velit esse molestie consequat, vel illum dolore eu feugiat nulla facilisis at vero eros et accumsan et iusto odio dignissim qui blandit praesent luptatum zzril delenit augue duis dolore te feugait nulla facilisi.</p>
  </div>
</section>

<section class="slide" style="left:597px;top:525px">
  <div class="title" style="left:72px;top:12px"><span class="hl">YOUR</span> PROJECTS</div>
  <svg width="66" height="56" viewBox="0 0 66 56" style="left:21px;top:65px">
    <rect x="0" y="0" width="64" height="44" rx="3" fill="#c8c9cb"/>
    <rect x="3" y="3" width="58" height="36" fill="#ececec"/>
    <circle cx="32" cy="42" r="1.6" fill="#3c3c3e"/>
    <path d="M28 44 h8 l1.5 7 h-11z" fill="#b5b6b8"/><rect x="22" y="50" width="20" height="3" fill="#a7a9ac"/>
  </svg>
  <div class="logo" style="left:27px;top:77px;font-size:10px"><span class="dot"></span><span><span class="name">NOVARA</span><span class="tag">TECHNOLOGIES</span></span></div>
  <svg width="22" height="100" viewBox="0 0 22 100" style="left:112px;top:49px">
    <g fill="none" stroke="#ff8200" stroke-width="2.8">
      <path d="M11 6 c-3 -4 -9 -4 -9 0 s6 4 9 0 s9 -4 9 0 s-6 4 -9 0z"/>
      <path d="M11 32 c-3 -4 -9 -4 -9 0 s6 4 9 0 s9 -4 9 0 s-6 4 -9 0z"/>
      <path d="M11 58 c-3 -4 -9 -4 -9 0 s6 4 9 0 s9 -4 9 0 s-6 4 -9 0z"/>
      <path d="M11 84 c-3 -4 -9 -4 -9 0 s6 4 9 0 s9 -4 9 0 s-6 4 -9 0z"/>
    </g>
  </svg>
  <div class="body" style="left:140px;top:45px;width:131px">Lorem ipsum dolor sit amet, consectetuer adipiscing elit, sed diam nonummy nibh euismod tincidunt ut laoreet dolore magna aliquam erat volutpat.</div>
  <div class="body" style="left:140px;top:71px;width:131px">Ut wisi enim ad minim veniam, quis nostrud exerci tation ullamcorper suscipit lobortis nisl ut aliquip ex ea commodo consequat.</div>
  <div class="body" style="left:140px;top:97px;width:131px">Duis autem vel eum iriure dolor in hendrerit in vulputate velit esse molestie consequat, vel illum dolore eu feugiat nulla facilisis at vero</div>
  <div class="body" style="left:140px;top:123px;width:131px">Eros et accumsan et iusto odio dignissim qui blandit praesent luptatum zzril delenit augue duis dolore te feugait nulla facilisi.</div>
</section>

<!-- Row 4 -->
<section class="slide compare" style="left:7px;top:694px">
  <div class="title" style="left:0;top:8px;width:285px;text-align:center">COMAPRISON</div>
  <div class="box prob">
    <h4>PROBLEMS</h4>
    <svg width="20" height="20" viewBox="0 0 20 20" style="left:52px;top:16px"><g fill="#3c3c3e"><circle cx="15" cy="4" r="3"/><circle cx="4" cy="10" r="3"/><circle cx="15" cy="16" r="3"/></g><path d="M15 4 L4 10 L15 16" stroke="#3c3c3e" stroke-width="2" fill="none"/></svg>
    <div style="height:22px"></div>
    <p>Lorem ipsum dolor sit amet, consectetuer adipiscing elit</p>
    <p>sed diam nonummy nibh euismod tincidunt ut laoreet dolore magna aliquam erat volutpat.</p>
    <p>Ut wisi enim ad minim veniam, quis nostrud exerci tation ullamcorper suscipit</p>
    <p>lobortis nisl ut aliquip ex ea commodo consequat.</p>
  </div>
  <div class="box sol">
    <h4>SOLUTIONS</h4>
    <svg width="26" height="14" viewBox="0 0 26 14" style="left:49px;top:19px"><rect x="1" y="1" width="21" height="12" rx="2" fill="none" stroke="#fff" stroke-width="2"/><rect x="23" y="4.5" width="2.5" height="5" fill="#fff"/><rect x="4" y="4" width="3" height="6" fill="#fff"/><rect x="8.5" y="4" width="3" height="6" fill="#fff"/><rect x="13" y="4" width="3" height="6" fill="#fff"/></svg>
    <div style="height:22px"></div>
    <p>Lorem ipsum dolor sit amet, consectetuer adipiscing elit</p>
    <p>sed diam nonummy nibh euismod tincidunt ut laoreet dolore magna aliquam erat volutpat.</p>
    <p>Ut wisi enim ad minim veniam, quis nostrud exerci tation ullamcorper suscipit</p>
    <p>lobortis nisl ut aliquip ex ea commodo consequat.</p>
  </div>
</section>

<section class="slide team" style="left:302px;top:694px">
  <div class="title" style="left:17px;top:10px">YOUR <span class="hl">TEAM</span></div>
  <div class="logo" style="right:10px;top:13px;font-size:12px"><span class="dot"></span><span><span class="name">NOVARA</span><span class="tag">TECHNOLOGIES</span></span></div>
  <div class="pic" style="left:12px" role="img" aria-label="Portrait of team member one in a blue suit"></div>
  <div class="pic" style="left:80px" role="img" aria-label="Portrait of team member two in a dark suit"></div>
  <div class="pic" style="left:148px" role="img" aria-label="Portrait of team member three in a denim shirt"></div>
  <div class="pic" style="left:216px" role="img" aria-label="Portrait of team member four in a white jacket"></div>
  <div class="who" style="left:12px">Name 01<br>Lorem ipsum</div>
  <div class="who on" style="left:80px">Name 02<br>Lorem ipsum</div>
  <div class="who" style="left:148px">Name 03<br>Lorem ipsum</div>
  <div class="who" style="left:216px">Name 04<br>Lorem ipsum</div>
</section>

<section class="slide" style="left:597px;top:694px">
  <div class="logo" style="left:12px;top:13px;font-size:13px"><span class="dot"></span><span><span class="name">NOVARA</span><span class="tag">TECHNOLOGIES</span></span></div>
  <div class="title" style="right:16px;top:10px">LOREM <span class="hl">IPSUM</span></div>
  <div class="sub" style="left:17px;top:47px">Subtitle 01</div>
  <div class="sub" style="left:141px;top:47px">Subtitle 02</div>
  <div class="body" style="left:16px;top:60px;width:100px">Lorem ipsum dolor sit amet, consectetuer adipiscing elit, sed diam nonummy nibh euismod tincidunt ut laoreet dolore magna aliquam erat volutpat. Ut wisi enim ad minim veniam, quis nostrud exerci tation ullamcorper suscipit lobortis nisl ut aliquip ex ea commodo consequat. Duis autem vel eum iriure dolor in hendrerit in vulputate velit esse molestie consequat, vel illum dolore eu feugiat nulla facilisis at vero eros et accumsan et iusto odio dignissim qui blandit praesent luptatum zzril delenit augue duis dolore te feugait nulla facilisi.</div>
  <div class="body" style="left:140px;top:60px;width:100px">Lorem ipsum dolor sit amet, consectetuer adipiscing elit, sed diam nonummy nibh euismod tincidunt ut laoreet dolore magna aliquam erat volutpat. Ut wisi enim ad minim veniam, quis nostrud exerci tation ullamcorper suscipit lobortis nisl ut aliquip ex ea commodo consequat. Duis autem vel eum iriure dolor in hendrerit in vulputate velit esse molestie consequat, vel illum dolore eu feugiat nulla facilisis at vero eros et accumsan et iusto odio dignissim qui blandit praesent luptatum zzril delenit augue duis dolore te feugait nulla facilisi.</div>
  <div class="abs" style="left:262px;top:46px;width:23px;height:93px;background:var(--dark)"></div>
  <svg width="10" height="18" viewBox="0 0 10 18" style="left:269px;top:84px"><rect x="1" y="1" width="8" height="16" rx="1.5" fill="none" stroke="#fff" stroke-width="1.4"/><circle cx="5" cy="14.5" r=".9" fill="#fff"/></svg>
</section>

<!-- Row 5 -->
<section class="slide" style="left:7px;top:862px">
  <div class="title" style="left:17px;top:12px"><span class="hl">PIE</span> CHART</div>
  <svg width="285" height="161" viewBox="0 0 285 161" style="left:0;top:0" font-family="Titillium Web, sans-serif" font-size="7">
    <circle cx="70" cy="92" r="52" fill="#e6e7e8"/>
    <path d="M70 92 L70 52 A40 40 0 0 1 108 79.6 Z" fill="#58595b"/>
    <path d="M70 92 L108 79.6 A40 40 0 0 1 82.4 130 Z" fill="#3c3c3e"/>
    <path d="M70 92 L82.4 130 A40 40 0 0 1 32 79.6 Z" fill="#ff8200"/>
    <path d="M70 92 L32 79.6 A40 40 0 0 1 70 52 Z" fill="#808285"/>
    <g fill="#fff" text-anchor="middle"><text x="62" y="73">20%</text><text x="89" y="79">20%</text><text x="87" y="109">25%</text><text x="50" y="103">35%</text></g>
  </svg>
  <div class="legend" style="top:9px;background:var(--grey)"><svg width="14" height="14" viewBox="0 0 14 14" style="position:static"><g fill="#fff"><circle cx="7" cy="3" r="2.3"/><path d="M3 14 v-6 a4 4 0 0 1 8 0 v6z"/><circle cx="2" cy="5" r="1.5"/><circle cx="12" cy="5" r="1.5"/></g></svg><span>Lorem ipsum dolor sit amet, consectetuer adipiscing elit</span></div>
  <div class="legend" style="top:45px;background:var(--dark)"><svg width="14" height="14" viewBox="0 0 14 14" style="position:static"><g fill="#fff"><circle cx="7" cy="3" r="2.3"/><path d="M3 14 v-6 a4 4 0 0 1 8 0 v6z"/><circle cx="2" cy="5" r="1.5"/><circle cx="12" cy="5" r="1.5"/></g></svg><span>Lorem ipsum dolor sit amet, consectetuer adipiscing elit</span></div>
  <div class="legend" style="top:82px;background:var(--dark)"><svg width="14" height="14" viewBox="0 0 14 14" style="position:static"><g fill="#fff"><circle cx="7" cy="3" r="2.3"/><path d="M3 14 v-6 a4 4 0 0 1 8 0 v6z"/><circle cx="2" cy="5" r="1.5"/><circle cx="12" cy="5" r="1.5"/></g></svg><span>Lorem ipsum dolor sit amet, consectetuer adipiscing elit</span></div>
  <div class="legend" style="top:118px;background:var(--orange)"><svg width="14" height="14" viewBox="0 0 14 14" style="position:static"><g fill="#fff"><circle cx="7" cy="3" r="2.3"/><path d="M3 14 v-6 a4 4 0 0 1 8 0 v6z"/><circle cx="2" cy="5" r="1.5"/><circle cx="12" cy="5" r="1.5"/></g></svg><span>Lorem ipsum dolor sit amet, consectetuer adipiscing elit</span></div>
</section>

<section class="slide" style="left:302px;top:862px">
  <div class="abs" style="left:8px;top:18px;width:275px;height:130px;background:radial-gradient(ellipse at 50% 45%,#e4e5e6 0%,#eeeeef 55%,#fff 80%)" role="img" aria-label="Light grey world map"></div>
  <div class="title" style="right:10px;top:12px"><span class="hl">AREA</span> CHART</div>
  <svg width="285" height="161" viewBox="0 0 285 161" style="left:0;top:0" font-family="Titillium Web, sans-serif" font-size="4.5" fill="#3c3c3e">
    <path d="M32 26 V134 H165" fill="none" stroke="#3c3c3e" stroke-width=".7"/>
    <g text-anchor="end"><text x="24" y="30">60</text><text x="24" y="52">50</text><text x="24" y="73">40</text><text x="24" y="94">30</text><text x="24" y="115">20</text><text x="24" y="136">0</text></g>
    <g stroke="#3c3c3e" stroke-width=".6"><path d="M29 28h3M29 50h3M29 71h3M29 92h3M29 113h3"/></g>
    <g text-anchor="middle"><text x="46" y="144">1</text><text x="75" y="144">2</text><text x="103" y="144">3</text><text x="132" y="144">4</text><text x="160" y="144">5</text></g>
    <polyline points="46,112 75,93 103,93 132,69 160,36" fill="none" stroke="#ff8200" stroke-width="1"/>
    <g fill="#ff8200"><circle cx="46" cy="112" r="1.5"/><circle cx="75" cy="93" r="1.5"/><circle cx="103" cy="93" r="1.5"/><circle cx="132" cy="69" r="1.5"/><circle cx="160" cy="36" r="1.5"/></g>
  </svg>
  <div class="body" style="left:188px;top:51px;width:76px">Lorem ipsum dolor sit amet, consectetuer adipiscing elit, sed diam nonummy nibh euismod tincidunt ut laoreet dolore magna aliquam erat volutpat. Ut wisi enim ad minim veniam, quis nostrud exerci tation ullamcorper suscipit lobortis nisl ut aliquip ex ea commodo consequat.</div>
  <div class="logo" style="right:12px;top:136px;font-size:12px"><span class="dot"></span><span><span class="name">NOVARA</span><span class="tag">TECHNOLOGIES</span></span></div>
</section>

<section class="slide" style="left:597px;top:862px">
  <div class="photo" style="inset:0;background:radial-gradient(ellipse at 55% 120%,#3b3a30 0%,#141c2b 45%,#05070c 100%)" role="img" aria-label="Night view of Earth from space with glowing city lights"></div>
  <div class="title" style="left:15px;top:12px;color:var(--orange);font-size:18px">TECHNOLOGY</div>
  <div class="sub" style="left:16px;top:36px;color:#fff">Subtitle</div>
  <svg width="22" height="18" viewBox="0 0 22 18" style="left:256px;top:8px"><g fill="none" stroke="#fff" stroke-width="2.2" stroke-linecap="round"><path d="M2 7 a13 13 0 0 1 18 0"/><path d="M5.5 10.5 a8 8 0 0 1 11 0"/></g><circle cx="11" cy="15" r="2" fill="#fff"/></svg>
  <div class="logo" style="left:16px;top:137px;font-size:11px"><span class="dot"></span><span class="name">NOVARA</span></div>
</section>

<!-- Row 6 -->
<section class="slide" style="left:7px;top:1028px">
  <div class="title" style="left:17px;top:10px"><span class="hl">BAR</span> CHART</div>
  <div class="abs" style="left:0;top:35px;width:158px;height:91px;background:var(--grey);border-radius:0 46px 46px 0"></div>
  <svg width="22" height="80" viewBox="0 0 22 80" style="left:9px;top:43px">
    <g fill="none" stroke="#c8c9cb" stroke-width="2.6">
      <path d="M11 8 c-3 -4 -9 -4 -9 0 s6 4 9 0 s9 -4 9 0 s-6 4 -9 0z"/>
      <path d="M11 31 c-3 -4 -9 -4 -9 0 s6 4 9 0 s9 -4 9 0 s-6 4 -9 0z"/>
      <path d="M11 54 c-3 -4 -9 -4 -9 0 s6 4 9 0 s9 -4 9 0 s-6 4 -9 0z"/>
    </g>
  </svg>
  <div class="body" style="left:40px;top:42px;width:100px;color:#fff">Lorem ipsum dolor sit amet, consectetuer adipiscing elit,</div>
  <div class="body" style="left:40px;top:63px;width:100px;color:#fff">sed diam nonummy nibh euismod tincidunt ut laoreet dolore magna aliquam erat volutpat.</div>
  <div class="body" style="left:40px;top:89px;width:100px;color:#fff">Ut wisi enim ad minim veniam, quis nostrud exerci tation ullamcorper suscipit lobortis nisl ut aliquip ex ea commodo consequat.</div>
  <div class="abs" style="left:173px;top:46px;width:26px;height:77px;background:var(--dark)"></div>
  <div class="abs" style="left:199px;top:20px;width:27px;height:103px;background:var(--orange)"></div>
  <div class="abs" style="left:226px;top:72px;width:26px;height:51px;background:var(--grey-mid)"></div>
  <svg width="285" height="161" viewBox="0 0 285 161" style="left:0;top:0" font-family="Titillium Web, sans-serif" font-size="6">
    <path d="M118 123 V148 H285" fill="none" stroke="#3c3c3e" stroke-width=".6" stroke-dasharray="1.5 1.5"/>
    <text transform="translate(189 140) rotate(-90)" fill="#3c3c3e">2016</text>
    <text transform="translate(215 140) rotate(-90)" fill="#ff8200">2017</text>
    <text transform="translate(241 140) rotate(-90)" fill="#808285">2018</text>
  </svg>
  <div class="logo" style="left:16px;top:135px;font-size:12px"><span class="dot"></span><span><span class="name">NOVARA</span><span class="tag">TECHNOLOGIES</span></span></div>
</section>

<section class="slide" style="left:302px;top:1028px">
  <div class="abs" style="left:37px;top:18px;width:205px;height:125px;border:2px solid var(--grey)"></div>
  <div class="abs" style="left:0;top:35px;width:285px;height:9px;background:var(--grey-light)"></div>
  <div class="abs" style="left:0;top:44px;width:285px;height:71px;background:var(--orange)"></div>
  <div class="abs" style="left:0;top:115px;width:285px;height:10px;background:var(--paper)"></div>
  <svg width="30" height="22" viewBox="0 0 30 22" style="left:17px;top:66px"><rect x="4" y="2" width="22" height="14" rx="1.5" fill="none" stroke="#fff" stroke-width="1.6"/><rect x="1" y="17" width="28" height="2.5" rx="1" fill="#fff"/></svg>
  <div class="abs" style="left:52px;top:58px;width:180px;font-size:6.8px;font-style:italic;color:#fff;text-align:center;line-height:1.32">“Lorem ipsum dolor sit amet, consectetuer adipiscing elit, sed diam nonummy nibh euismod tincidunt ut laoreet dolore magna aliquam erat volutpat. Ut wisi enim ad minim veniam”</div>
  <div class="abs" style="left:184px;top:103px;font-size:6.8px;font-style:italic;color:#fff">- Dolor sit amet</div>
</section>

<section class="slide" style="left:597px;top:1028px">
  <div class="photo" style="inset:0;background:linear-gradient(200deg,#cfd0d2 0%,#e6e7e8 45%,#f3f3f3 100%)" role="img" aria-label="Desk with a smartphone, keyboard, pen and notebook seen from above"></div>
  <div class="logo" style="left:8px;top:81px;font-size:20px"><span class="dot"></span><span><span class="name">NOVARA</span><span class="tag">TECHNOLOGIES</span></span></div>
  <div class="abs" style="left:12px;top:117px;font-size:6px;font-weight:700;color:var(--orange)">GET IN TOUCH</div>
  <div class="abs" style="left:23px;top:128px;font-size:6px;color:var(--ink);line-height:1.25">Mobile - 0 123 456 7890<br>Email - your@email.com<br>Web - yourwebsite.com</div>
</section>

</body>
</html>
```